Plakate für Haushaltsnahe Dienstleistungen sowie Alltagsbegleitung
Zielgruppe
Wir sind eine Firma die Haushaltsnahe Dienstleistungen sowie Alltagsbegleitung anbietet. Unser Hauptkundenklientel sind Pflegebedürftige Menschen denen Haushaltshilfe von der Pflegekasse zu steht.
Aufgabenstellung
Es soll ein Roll-Up werden. Es soll drauf stehen: Abrechnung mit allen Pflegekasse möglich über den Entlastungsbetrag (ab Pflegegrad 1 bis 5) sowie Verhinderungspflege. Kontaktdaten sowie unsere Vorteile sollen auch drauf stehen.

```html
<!DOCTYPE html>
<html lang="de">
<head>
<meta charset="utf-8">
<title>Roll-Up Hausanker Haushaltshilfen</title>
<link href="https://fonts.googleapis.com/css2?family=Fira+Sans:wght@400;500;600;700&display=swap" rel="stylesheet">
<style>
  :root{
    --bg:#c8c8c8;
    --paper:#ffffff;
    --red:#cc2a3b;
    --red-deep:#c22236;
    --berry:#b82a55;
    --dark:#4a4749;
    --ink:#333133;
  }
  *{box-sizing:border-box;margin:0;padding:0}
  html,body{width:1200px;height:1200px;overflow:hidden;background:var(--bg)}
  body{font-family:"Fira Sans",sans-serif;display:flex;align-items:center;justify-content:center}
  .rollup{position:relative;width:470px;height:1140px;background:var(--paper);overflow:hidden}
  .rollup__waves{position:absolute;inset:0;width:100%;height:100%}
  .brand{position:absolute;top:52px;left:0;right:0;display:flex;align-items:center;justify-content:center;gap:14px}
  .brand__dot{width:62px;height:62px;border-radius:50%;background:var(--red)}
  .brand__name{color:var(--red);font-weight:600;line-height:1.05}
  .brand__name strong{display:block;font-size:40px;letter-spacing:1px;font-weight:600}
  .brand__name span{display:block;font-size:14.5px;letter-spacing:1.2px;font-weight:600}
  .cta-badge{position:absolute;top:118px;right:34px;width:104px;height:104px;border-radius:50%;background:var(--dark);border:3px solid #fff;color:#fff;font-weight:600;font-size:14px;line-height:1.15;display:flex;align-items:center;justify-content:center;text-align:center}
  .headline{position:absolute;top:240px;left:0;right:0;text-align:center;color:#fff;font-weight:700;font-size:34px;letter-spacing:3px;line-height:1.25}
  .intro{position:absolute;top:338px;left:40px;right:40px;text-align:center;color:#fff;font-size:9px;letter-spacing:.6px;line-height:1.45}
  .benefits-band{position:absolute;top:410px;left:0;right:0;height:44px;background:#fff;display:flex;align-items:center;justify-content:center}
  .benefits-band h2{color:var(--red);font-size:32px;font-weight:700;letter-spacing:3px}
  .benefit{position:absolute;width:200px;text-align:center;color:#fff;font-weight:600;font-size:12.5px;letter-spacing:1.2px;line-height:1.45;text-transform:uppercase}
  .benefit__icon{width:132px;height:132px;margin:0 auto 14px;border-radius:50%;background:#fff;box-shadow:2px 4px 8px rgba(0,0,0,.25);display:flex;align-items:center;justify-content:center}
  .benefit__icon svg{width:84px;height:84px;fill:var(--red-deep)}
  .benefit--billing{top:480px;left:23px}
  .benefit--relief{top:480px;left:240px}
  .benefit--respite{top:730px;left:23px}
  .benefit--forms{top:730px;left:240px}
  .contact{position:absolute;left:0;right:0;text-align:center;color:var(--ink)}
  .contact--address{top:1010px}
  .contact--reach{top:1078px}
  .contact__title{font-weight:700;font-size:14px;letter-spacing:2px}
  .contact__line{font-size:13.5px;letter-spacing:1px;margin-top:3px;white-space:nowrap}
</style>
</head>
<body>
<main class="rollup">
  <svg class="rollup__waves" viewBox="0 0 470 1140" preserveAspectRatio="none" aria-hidden="true">
    <defs>
      <linearGradient id="stripe" x1="0" x2="1" y1="0" y2="0">
        <stop offset="0" stop-color="#cc2a3b"/>
        <stop offset="1" stop-color="#b82a55"/>
      </linearGradient>
    </defs>
    <path d="M0 130 Q180 190 470 155 L470 992 Q220 990 0 938 Z" fill="var(--red)"/>
    <path d="M0 130 Q180 190 470 155 L470 205 Q220 220 0 160 Z" fill="url(#stripe)"/>
  </svg>

  <header class="brand">
    <div class="brand__dot" aria-hidden="true"></div>
    <div class="brand__name"><strong>HAUSANKER</strong><span>HAUSHALTSHILFEN &amp; MEHR</span></div>
  </header>

  <div class="cta-badge">Jetzt Termin<br>vereinbaren!</div>

  <h1 class="headline">BENÖTIGEN SIE<br>HILFE IM HAUSHALT?</h1>
  <p class="intro">Wir bieten Haushaltshilfen und Alltagsbegleiter für Privathaushalte an. Unsere Hauptkundenklientel sind Pflegebedürftige Menschen denen eine Haushaltshilfe von der Pflegekasse zusteht. Weitere Kunden sind Familien und/oder Singlehaushalte, die eine Haushaltshilfe benötigen.</p>

  <div class="benefits-band"><h2>UNSERE VORTEILE</h2></div>

  <section class="benefit benefit--billing">
    <div class="benefit__icon">
      <svg viewBox="0 0 64 64" aria-hidden="true">
        <path d="M14 4h24l14 14v38a4 4 0 0 1-4 4H14a4 4 0 0 1-4-4V8a4 4 0 0 1 4-4z"/>
        <path d="M38 4v14h14" fill="#fff"/>
        <rect x="16" y="12" width="12" height="4" rx="2" fill="#fff"/>
        <rect x="16" y="20" width="8" height="4" rx="2" fill="#fff"/>
        <text x="31" y="52" font-size="24" font-weight="700" text-anchor="middle" fill="#fff" font-family="Fira Sans, sans-serif">$</text>
      </svg>
    </div>
    Abrechnung mit allen Pflegekassen möglich
  </section>

  <section class="benefit benefit--relief">
    <div class="benefit__icon">
      <svg viewBox="0 0 64 64" aria-hidden="true">
        <path d="M26 4h10v10h10v10H36v10H26V24H16V14h10z"/>
        <path d="M4 44h14c4 0 6 2 10 2h10c3 0 3 4 0 4H26h14l14-9c3-2 7 1 4 4L42 56H8a4 4 0 0 1-4-4z"/>
      </svg>
    </div>
    Abrechnung über den Entlastungsbetrag von mind. 125 € mtl. ab Pflegegrad 1 möglich
  </section>

  <section class="benefit benefit--respite">
    <div class="benefit__icon">
      <svg viewBox="0 0 64 64" aria-hidden="true">
        <path d="M32 32 20 20a7 7 0 0 1 12-10 7 7 0 0 1 12 10z"/>
        <path d="M4 44h14c4 0 6 2 10 2h10c3 0 3 4 0 4H26h14l14-9c3-2 7 1 4 4L42 56H8a4 4 0 0 1-4-4z"/>
      </svg>
    </div>
    Auch über die Verhinderungspflege
  </section>

  <section class="benefit benefit--forms">
    <div class="benefit__icon">
      <svg viewBox="0 0 64 64" aria-hidden="true">
        <path d="M10 4h22l14 14v38a4 4 0 0 1-4 4H10a4 4 0 0 1-4-4V8a4 4 0 0 1 4-4z"/>
        <path d="M32 4v14h14" fill="#fff"/>
        <path d="M12 48c3-8 5-8 6-2s3 4 5-1 3 2 6 2" stroke="#fff" stroke-width="2.5" fill="none"/>
        <path d="M52 20l6 6-22 22-9 3 3-9z" stroke="#fff" stroke-width="2.5"/>
      </svg>
    </div>
    Hilfe bei der Antragsstellung
  </section>

  <footer>
    <div class="contact contact--address">
      <p class="contact__title">HAUSANKER HAUSHALTSHILFEN &amp; MEHR</p>
      <p class="contact__line">Lindenweg 14 | 70599 Musterstadt</p>
    </div>
    <div class="contact contact--reach">
      <p class="contact__title">KONTAKT</p>
      <p class="contact__line">0711 98765432 | info@hausanker.de | www.hausanker.de</p>
    </div>
  </footer>
</main>
</body>
</html>
```